Health Benefits Association Website Design

The Unified Household Wellspring Alliance (UHWA) is an organization formed for the purpose of providing its members better value for selected health benefits and services. Members can use the association benefits either in conjunction with or independently of other medical insurance they may have. Some of the benefits available include discounted dental and vision care and prescription mail order services. There is no limitation on who can join. This membership will be primarily marketed as a way to enhance the value of a fixed benefit health insurance plan although members do not have to have the insurance plan join the association.

We are seeking a design for a website to be used for consumers to get information about membership and for current members to be able to access their benefits. The website should include:

1) A landing page to provide a description of the UHWA

2) A secondary page that can be duplicated that will:
a. Provide a list of benefits
b. Provide a membership enrollment form
c. Provide a member’s only access page
d. Provide a contact page for more information

We are seeking a modern but conservative design that will reflect value, simplicity and good health. The site design will also need to be compatible for use with mobile phones and tablets.

A copy of the association logo is included with the submission. It will also need to be incorporated into the website design. Layouts of similar association websites have also been included for reference.

Target Market(s)

Ages 25 to 65 unmarried, married with no children, professionals, self-employed, active and healthy

Industry/Entity Type

Health And Wellness

Number of Pages Required

2 page

Font styles to use
Sans Serif

Colors

Designer to choose colors to be used in the design.

Requirements
Must have
• UHWA Logo (attached). Use colors from the logo in the website design.
Nice to have
• Graphics, if used, should convey health and fitness and skew toward a diverse array of adults 25 to 40.

```html
<!DOCTYPE html>
<html lang="en">
<head>
<meta charset="utf-8">
<title>Unified Household Wellspring Alliance</title>
<link href="https://fonts.googleapis.com/css2?family=Raleway:wght@300;400;500;600;700&display=swap" rel="stylesheet">
<style>
:root{
  --yellow:#f6cd00;
  --yellow-dark:#dcb300;
  --olive:#8d984a;
  --olive-light:#a3ad5e;
  --ink:#1f1f1f;
  --text:#3a3a3a;
  --grey-bg:#f2f1f2;
  --white:#ffffff;
  --night:#111111;
}
*{margin:0;padding:0;box-sizing:border-box}
html,body{width:1200px;height:2521px;overflow:hidden}
body{font-family:"Raleway",Arial,sans-serif;color:var(--text);background:var(--white);position:relative}
.abs{position:absolute}

/* hero */
.hero{left:0;top:0;width:1200px;height:593px;background:linear-gradient(100deg,#4f7a6a 0%,#8fb3a4 30%,#c9d6cf 55%,#e9ece8 70%,#6b7f5a 100%)}
.topbar{top:18px;right:0;width:1200px;height:26px;font-size:14px;color:var(--white)}
.topbar .item{position:absolute;top:2px;display:flex;align-items:center;gap:8px}
.topbar .dot{width:16px;height:16px;border-radius:50%;background:var(--yellow)}
.navband{left:0;top:59px;width:1200px;height:67px;background:rgba(0,0,0,.72)}
.nav{position:absolute;top:23px;right:86px;display:flex;font-size:14px;color:var(--white)}
.nav a{color:var(--white);text-decoration:none;padding:0 28px;border-left:1px solid rgba(255,255,255,.35)}
.nav a:first-child{border-left:none}
.brand{left:86px;top:12px;width:104px;height:120px;display:flex;flex-direction:column;align-items:center;justify-content:center;gap:6px;text-align:center}
.brand .mark{width:30px;height:30px;border-radius:50%;background:var(--yellow)}
.brand .name{font-size:13px;font-weight:700;color:var(--yellow);line-height:1.1}
.hero-title{top:278px;left:0;width:1200px;text-align:center;font-size:36px;font-weight:400;color:var(--yellow)}
.hero-text{top:340px;left:270px;width:660px;text-align:center;font-size:15px;line-height:25px;color:#1c1c1c}
.btn-outline{display:flex;align-items:center;justify-content:center;border:2px solid var(--olive);border-radius:30px;color:var(--ink);font-size:14px}
.hero-btn{left:524px;top:417px;width:152px;height:40px;border-color:var(--yellow)}
.slider-dots{left:51px;top:320px;display:flex;flex-direction:column;gap:9px}
.slider-dots span{width:9px;height:9px;border-radius:50%;background:rgba(255,255,255,.7)}
.slider-dots span.on{background:var(--olive-light)}

/* benefits */
.benefits{left:0;top:593px;width:1200px;height:650px;background:var(--grey-bg);box-shadow:0 10px 14px rgba(0,0,0,.08)}
.section-title{font-size:35px;font-weight:400;color:var(--ink)}
.rule{height:2px;width:44px;background:var(--olive)}
.card{top:207px;width:324px;height:344px;background:var(--white);border:1px solid #dcdcdc;text-align:center}
.card .photo{width:100%;height:183px}
.card .icon{position:absolute;left:141px;top:166px;width:42px;height:42px;border-radius:50%;background:var(--white);display:flex;align-items:center;justify-content:center}
.card h3{position:absolute;top:226px;width:100%;font-size:11px;font-weight:700;color:var(--ink);letter-spacing:.2px}
.card .rule{position:absolute;left:146px;top:247px;width:32px;height:1px}
.card p{position:absolute;top:258px;left:40px;width:244px;font-size:11px;line-height:15px;color:#555}
.card .btn-outline{position:absolute;left:116px;top:303px;width:92px;height:24px;font-size:10px;border-width:1.5px}
.pager{left:579px;top:598px;display:flex;gap:6px}
.pager span{width:9px;height:9px;border-radius:50%;background:#d5d5d5}
.pager span.on{background:var(--olive)}

/* about */
.about-title{left:92px;top:1345px}
.about-text{left:86px;top:1432px;width:450px;font-size:13px;line-height:18.5px;color:#333}
.about-btn{left:87px;top:1640px;width:142px;height:38px;font-size:15px}
.about-photo{left:601px;top:1347px;width:512px;height:400px;background:linear-gradient(120deg,#e9e4dd 0%,#f4f1ec 45%,#d9cfc2 70%,#c6b8a5 100%)}

/* members band */
.members{left:0;top:1828px;width:1200px;height:116px;background:var(--yellow)}
.member-photo{left:87px;top:1747px;width:118px;height:197px;background:linear-gradient(180deg,#d8c7b4 0%,#3a3d45 45%,#20232a 100%);border-radius:50px 50px 0 0}
.members h2{position:absolute;left:240px;top:30px;font-size:31px;font-weight:400;color:var(--ink)}
.members p{position:absolute;left:244px;top:75px;font-size:14px;color:#3a3300}
.login{left:894px;top:1856px;width:218px;height:61px;border-radius:31px;background:var(--yellow-dark);border:1px solid #c9a300;display:flex;align-items:center;justify-content:center;font-size:26px;color:var(--ink);letter-spacing:1px}

/* contact */
.contact{left:0;top:1944px;width:1200px;height:497px;background:radial-gradient(ellipse at 70% 40%,#8a8a4c 0%,#5e6230 45%,#3e4022 100%)}
.contact .heading{font-size:28px;font-weight:400;color:var(--white)}
.contact .rule{background:rgba(255,255,255,.7);width:92px;height:1px}
.info{left:87px;width:460px;height:60px}
.info .badge{position:absolute;left:0;top:0;width:54px;height:54px;border-radius:50%;background:var(--olive);display:flex;align-items:center;justify-content:center}
.info h4{position:absolute;left:83px;top:-2px;font-size:17px;font-weight:700;color:var(--white)}
.info span{position:absolute;left:83px;top:25px;font-size:16px;color:#eee}
.steps-line{left:113px;top:2140px;width:2px;height:240px;background:rgba(255,255,255,.35)}
.divider{left:583px;top:2058px;width:1px;height:282px;background:rgba(255,255,255,.4)}
.field{left:659px;width:430px;border-bottom:1px solid rgba(255,255,255,.55);font-size:11px;color:#eee;padding-bottom:8px}
.submit{left:659px;top:2344px;width:430px;height:42px;background:var(--olive);color:var(--white);font-size:15px;display:flex;align-items:center;justify-content:center;letter-spacing:.5px}

/* footer */
.footer{left:0;top:2441px;width:1200px;height:80px;background:var(--night);text-align:center;color:#ddd}
.footer nav{position:absolute;top:22px;width:100%;display:flex;justify-content:center;gap:16px;font-size:12px}
.footer small{position:absolute;top:47px;width:100%;font-size:11px;color:#bbb}
</style>
</head>
<body>

<section class="abs hero" role="img" aria-label="Photo of a woman meditating beside a lake"></section>
<svg class="abs" style="left:0;top:500px" width="1200" height="94" viewBox="0 0 1200 94" aria-hidden="true">
  <path d="M0 94 L470 94 Q520 88 548 70 L560 60 L572 22 L584 60 Q600 76 620 70 Q650 80 690 86 Q760 94 1200 94 Z" fill="#f2f1f2"/>
</svg>

<div class="abs navband"></div>
<div class="abs topbar">
  <div class="item" style="left:782px"><span class="dot"></span>hello@wellspringhelp.org</div>
  <div class="item" style="left:988px;font-weight:700;font-size:15px"><span class="dot"></span>(555) 210-4836</div>
</div>
<div class="abs brand">
  <span class="mark"></span>
  <span class="name">UNIFIED HOUSEHOLD WELLSPRING</span>
</div>
<nav class="abs navband" style="background:none">
  <div class="nav"><a>Home</a><a>Benifits</a><a>Enrollment</a><a>Member's Page</a><a>Contact Us</a></div>
</nav>

<h1 class="abs hero-title">Nurturing Body and Mind.</h1>
<p class="abs hero-text">Lorem ipsum dolor. Sit amet pellentesque. Nec sociis urna. Dui quam vestibulum. Luctus a vel scelerisque ornare vivamus. Eleifend in cubilia.</p>
<a class="abs btn-outline hero-btn">Learn More</a>
<div class="abs slider-dots"><span></span><span class="on"></span><span></span></div>

<section class="abs benefits">
  <h2 class="abs section-title" style="top:68px;width:1200px;text-align:center">Benifits Membership</h2>
  <div class="abs rule" style="left:578px;top:121px"></div>
  <p class="abs" style="top:134px;width:1200px;text-align:center;font-size:12px;color:#333">Membership in UHWA provides a variety of benefits and resources, designed to save you money so you can focus on your family and business.</p>

  <article class="abs card" style="left:87px">
    <div class="photo" role="img" aria-label="Photo of a woman doing yoga in a green field" style="background:linear-gradient(180deg,#c9d8dc 0%,#9fb57a 45%,#6f8f3c 100%)"></div>
    <div class="icon"><svg width="26" height="26" viewBox="0 0 26 26"><path d="M13 22 C4 16 3 8 8 6 C11 5 13 8 13 8 C13 8 15 5 18 6 C23 8 22 16 13 22Z" fill="none" stroke="#8d984a" stroke-width="1.8"/></svg></div>
    <h3>HEALTH AND WELL-BEING SERVICES</h3><div class="rule"></div>
    <p>Lorem ipsum dolor. Sit amet pellentesque. Nec sociis urna. Dui quam vestibulum. Luctus a vel</p>
    <a class="btn-outline">Learn More</a>
  </article>
  <article class="abs card" style="left:438px">
    <div class="photo" role="img" aria-label="Photo of a smiling couple" style="background:linear-gradient(120deg,#6b4a3a 0%,#c99b7e 45%,#e6d6c8 75%,#bfb3a8 100%)"></div>
    <div class="icon"><svg width="26" height="26" viewBox="0 0 26 26"><rect x="4" y="9" width="18" height="12" rx="2" fill="none" stroke="#8d984a" stroke-width="1.8"/><path d="M10 9 V6 H16 V9" fill="none" stroke="#8d984a" stroke-width="1.8"/></svg></div>
    <h3>BUSINESS SERVICES</h3><div class="rule"></div>
    <p>Lorem ipsum dolor. Sit amet pellentesque. Nec sociis urna. Dui quam vestibulum. Luctus a vel</p>
    <a class="btn-outline">Learn More</a>
  </article>
  <article class="abs card" style="left:790px">
    <div class="photo" role="img" aria-label="Photo of a plated salmon dish with potatoes" style="background:linear-gradient(120deg,#f1f1ef 0%,#d9b56c 40%,#c8643a 55%,#5e7a32 75%,#e8e8e6 100%)"></div>
    <div class="icon"><svg width="26" height="26" viewBox="0 0 26 26"><path d="M5 20 H21 M8 20 V12 H18 V20 M10 12 V6 H16 V12" fill="none" stroke="#8d984a" stroke-width="1.8"/></svg></div>
    <h3>LIFESTYLE SERVICES</h3><div class="rule"></div>
    <p>Lorem ipsum dolor. Sit amet pellentesque. Nec sociis urna. Dui quam vestibulum. Luctus a vel</p>
    <a class="btn-outline">Learn More</a>
  </article>
  <div class="abs pager"><span></span><span class="on"></span><span></span></div>
</section>

<h2 class="abs section-title about-title">About Us</h2>
<div class="abs rule" style="left:87px;top:1398px;width:66px;height:1px"></div>
<p class="abs about-text">For over 70 years, Harlow Estates has been privilaged to serve the Central Savannah River Area and the greater Southest, providing real development and brokerage service. Our goal has been and continues to beto assist you, the property owners and buyers, in attaining both your personal andfinancial goals.<br>We believe that there is incalculable value in experienced dedication, wheather you're ready to act on aproperty, or just getting started with the process, we would love to have a conversation should our services be of benefit to you.</p>
<a class="abs btn-outline about-btn">Learn More</a>
<div class="abs about-photo" role="img" aria-label="Photo of two women relaxing in white robes at a spa"></div>

<section class="abs members">
  <h2>Informations for Only Members</h2>
  <p>Lorem ipsum dolor. Sit amet pellentesque. Nec sociis urna. Dui quam vestibulum. Luctus a vel</p>
</section>
<div class="abs member-photo" role="img" aria-label="Photo of a businessman in a dark suit"></div>
<a class="abs login">LOGIN</a>

<section class="abs contact" role="img" aria-label="Soft blurred photo of hands in green light"></section>
<h2 class="abs heading contact" style="background:none;left:87px;top:2014px;width:auto;height:auto" >Contact Us</h2>
<div class="abs rule" style="left:87px;top:2058px;width:92px;height:1px;background:rgba(255,255,255,.7)"></div>
<div class="abs steps-line"></div>

<div class="abs info" style="top:2088px">
  <div class="badge"><svg width="20" height="22" viewBox="0 0 20 22"><path d="M10 21 C4 13 3 10 3 8 A7 7 0 0 1 17 8 C17 10 16 13 10 21Z" fill="#fff"/><circle cx="10" cy="8" r="2.6" fill="#8d984a"/></svg></div>
  <h4>Address</h4><span>418 Birchwood Lane, Fairview, OH</span>
</div>
<div class="abs info" style="top:2169px">
  <div class="badge"><svg width="20" height="20" viewBox="0 0 20 20"><path d="M4 2 L8 2 L9 6 L7 8 C8 11 9 12 12 13 L14 11 L18 12 L18 16 C18 17 17 18 16 18 C8 18 2 12 2 4 C2 3 3 2 4 2Z" fill="#fff"/></svg></div>
  <h4>Phone</h4><span>0800 55 1234</span>
</div>
<div class="abs info" style="top:2249px">
  <div class="badge"><svg width="20" height="16" viewBox="0 0 20 16"><rect x="1" y="2" width="18" height="12" fill="#fff"/><path d="M1 2 L10 9 L19 2" fill="none" stroke="#8d984a" stroke-width="1.5"/></svg></div>
  <h4>Email</h4><span>contact@householdwellspring.org</span>
</div>
<div class="abs info" style="top:2330px">
  <div class="badge"><svg width="20" height="20" viewBox="0 0 20 20"><circle cx="10" cy="10" r="8.5" fill="#fff"/><path d="M10 5 V10 L13 12" fill="none" stroke="#8d984a" stroke-width="1.8"/></svg></div>
  <h4>Opening Hours</h4><span>Mon-Fri: 8:00 AM – 9:00 PM</span>
</div>

<div class="abs divider"></div>

<h2 class="abs" style="left:659px;top:2012px;font-size:28px;font-weight:400;color:#fff">Enroll Membership</h2>
<div class="abs rule" style="left:659px;top:2058px;width:92px;height:1px;background:rgba(255,255,255,.7)"></div>
<div class="abs field" style="top:2100px">Name..</div>
<div class="abs field" style="top:2156px">Email..</div>
<div class="abs field" style="top:2211px">Phone No..</div>
<div class="abs field" style="top:2266px;height:52px">Massege..</div>
<a class="abs submit">SUBMIT</a>

<footer class="abs footer">
  <nav><span>Home</span><span>Benifits</span><span>Enrollment</span><span>Member's Page</span><span>Contact Us</span></nav>
  <small>householdwellspring.org 2017. All rights reserved</small>
</footer>

</body>
</html>
```